Building company buisness cards

We are looking for a sharp modern new look for our business cards.
We are a New Zealand based company that specialises in house and land packages.
We have attached a photo of the current logo and would like to see if it can be improved somehow if needed.
We are open to any colours but we have chosen green at this stage.
Feel free to change the font and make the logo smarter looking.
Play with the colours and see what looks best.

We want a card that looks so good know one will want to throw it away!

Target Market(s)

Home buyers

Industry/Entity Type

Building

Contact Information for Business Card

Dorian Keswick
0217392604
dkeswick@tidewellhomecraft.co.nz
tidewellhomecraft.co.nz

Font styles to use
Serif
Sans Serif

Colors

Designer to choose colors to be used in the design.

Requirements
Must have
• Logo and company name on one side, details on the other side
Nice to have
• Color codes for the original green are HEX #4a8028, RGB(74,128,40), CMYK(42,0,69,50)
• Round corners, Raised and/or spot UV

```html
<!DOCTYPE html>
<html lang="en">
<head>
<meta charset="utf-8">
<title>Tidewell Homecraft — Business Cards</title>
<link rel="stylesheet" href="https://fonts.googleapis.com/css2?family=Oswald:wght@500&family=Open+Sans:wght@300&display=swap">
<style>
  :root {
    --backdrop: #1d1d1d;
    --card-green: #2f5f2c;
    --silver: #c9c9c9;
    --silver-soft: #b5b8b4;
    --rule: rgba(210, 210, 210, 0.55);
  }
  * { margin: 0; padding: 0; box-sizing: border-box; }
  html, body {
    width: 1200px;
    height: 895px;
    overflow: hidden;
    background: var(--backdrop);
  }
  .sheet {
    width: 1200px;
    height: 895px;
    display: flex;
    flex-direction: column;
    align-items: center;
    justify-content: center;
    gap: 40px;
  }
  .card {
    width: 630px;
    height: 350px;
    background: var(--card-green);
    border-radius: 6px;
    box-shadow: 0 14px 30px rgba(0, 0, 0, 0.55);
    display: flex;
    flex-direction: column;
    align-items: center;
    justify-content: center;
  }
  .brand-mark {
    display: flex;
    align-items: center;
    gap: 16px;
  }
  .brand-square {
    width: 18px;
    height: 18px;
    background: var(--silver);
  }
  .brand-name {
    font-family: "Oswald", sans-serif;
    font-weight: 500;
    font-size: 34px;
    line-height: 1;
    letter-spacing: 4px;
    text-transform: uppercase;
    color: var(--silver);
  }
  .brand-rule {
    width: 130px;
    height: 1px;
    background: var(--rule);
    margin-top: 24px;
  }
  .contact {
    display: flex;
    flex-direction: column;
    align-items: center;
    margin-top: 70px;
  }
  .contact-name {
    font-family: "Oswald", sans-serif;
    font-weight: 500;
    font-size: 30px;
    letter-spacing: 2px;
    text-transform: uppercase;
    color: var(--silver);
  }
  .contact-rule {
    width: 230px;
    height: 1px;
    background: var(--rule);
    margin: 6px 0 4px;
  }
  .contact-line {
    font-family: "Open Sans", sans-serif;
    font-weight: 300;
    color: var(--silver-soft);
    font-size: 15px;
    line-height: 1.35;
  }
  .contact-phone { font-size: 22px; color: var(--silver); }
</style>
</head>
<body>
  <main class="sheet">
    <section class="card card-front" aria-label="Card front">
      <div class="brand-mark">
        <span class="brand-square"></span>
        <h1 class="brand-name">Tidewell Homecraft</h1>
      </div>
      <div class="brand-rule"></div>
    </section>

    <section class="card card-back" aria-label="Card back">
      <div class="contact">
        <h2 class="contact-name">Dorian Keswick</h2>
        <div class="contact-rule"></div>
        <p class="contact-line contact-phone">0217392604</p>
        <p class="contact-line">dkeswick@tidewellhomecraft.co.nz</p>
        <p class="contact-line">tidewellhomecraft.co.nz</p>
      </div>
    </section>
  </main>
</body>
</html>
```